I need a design for "custom packing tape" for www.tarpexdirect.com® an industrial/commercial led li...

Here, are some ideas I was looking into before I decide to have all my tapes custom printed: (https://blog.querant.com/how-to-tape-shipping-box), (https://blog.querant.com/gummed-tape-vs-plastic-tape) Please visit the tarpexdirect page for more information (PDFs) on pakages dimensions. We have the tarpexdirect® logo attached to this project.

Target Market(s)

Industrial and commercial LED light market.

Industry/Entity Type

Light Industrial

Font styles to use
Other font styles liked:
• NO, let the designer pic it.

Colors

Designer to choose colors to be used in the design.

Requirements
Must have
• must have the ® included on all submissions. Also looks good on kraft paper and plastic. Black art on clear tape is a welcome option.
Nice to have
• some idea generators:
• https://blog.querant.com/how-to-tape-shipping-box
• https://blog.querant.com/gummed-tape-vs-plastic-tape
• https://brushwaystock.com/ (Packing tape mockups)
• https://blog.querant.com/practical-guide-to-designing-packing-tape
Should not have
• should not be without mockups of the logo applied to rolls and boxes.

```html
<!DOCTYPE html>
<html lang="en">
<head>
<meta charset="utf-8">
<title>tarpexdirect packing tape</title>
<link rel="stylesheet" href="https://fonts.googleapis.com/css2?family=Lato:wght@700&display=swap">
<style>
  :root {
    --backdrop: #b67424;
    --backdrop-light: #d39a4c;
    --tape-orange: #f2a42a;
    --tape-highlight: #f8c574;
    --brand-brown: #9b5230;
    --icon-tone: #c8742a;
    --band-black: #1f1f1f;
  }
  html, body {
    margin: 0;
    padding: 0;
    width: 1200px;
    height: 1200px;
    overflow: hidden;
  }
  body {
    background: linear-gradient(180deg, var(--backdrop) 0%, var(--backdrop-light) 100%);
    font-family: "Lato", Arial, sans-serif;
  }
  .canvas {
    position: relative;
    width: 1200px;
    height: 1200px;
  }
  .tape-strip {
    position: absolute;
    left: 0;
    top: 430px;
    width: 1200px;
    height: 340px;
    background: linear-gradient(180deg, var(--tape-highlight) 0%, var(--tape-orange) 40%, #e99a22 100%);
  }
  .icon-column {
    position: absolute;
    top: 20px;
    width: 110px;
    height: 300px;
    border-radius: 4px;
    background: linear-gradient(180deg, var(--icon-tone) 0%, #b8661f 100%);
    opacity: 0.5;
  }
  .icon-column--left { left: 30px; }
  .icon-column--right { left: 1060px; }
  .peel-band {
    position: absolute;
    left: 190px;
    top: 0;
    width: 86px;
    height: 340px;
    background: var(--band-black);
    display: flex;
    align-items: center;
    justify-content: center;
  }
  .peel-label {
    writing-mode: vertical-rl;
    transform: rotate(180deg);
    margin: 0;
    font-size: 34px;
    font-weight: 700;
    letter-spacing: 5px;
    color: var(--tape-orange);
  }
  .brand-block {
    position: absolute;
    left: 320px;
    top: 0;
    width: 700px;
    height: 340px;
    display: flex;
    flex-direction: column;
    justify-content: center;
    align-items: flex-start;
  }
  .brand-name {
    margin: 0;
    font-size: 104px;
    font-weight: 700;
    letter-spacing: -1px;
    color: var(--brand-brown);
    line-height: 1;
  }
  .brand-name .reg {
    font-size: 40px;
    vertical-align: top;
    margin-left: 4px;
  }
  .brand-domain {
    margin: 6px 0 0 0;
    align-self: flex-end;
    padding-right: 60px;
    font-size: 38px;
    font-weight: 700;
    color: var(--brand-brown);
    line-height: 1;
  }
</style>
</head>
<body>
  <main class="canvas">
    <section class="tape-strip" aria-label="Custom packing tape print">
      <div class="icon-column icon-column--left" role="img" aria-label="Line drawings of LED bulbs, corn lamps and panel fixtures"></div>
      <div class="peel-band">
        <p class="peel-label">PEEL HERE</p>
      </div>
      <div class="brand-block">
        <p class="brand-name">tarpexdirect<span class="reg">®</span></p>
        <p class="brand-domain">.com</p>
      </div>
      <div class="icon-column icon-column--right" role="img" aria-label="Line drawings of LED bulbs, corn lamps and panel fixtures"></div>
    </section>
  </main>
</body>
</html>
```